IT Distribution Wholesale Business Card & Logo Design

I need both logo and a business card that suits our business model, am happy to pay more for great effort put in.
Brevon Orbital Australia Pty Ltd
An IT Distribution / Wholesale company that distributes technology hardwares, softwares, components, etc.
Offer drop ship services for online retailers and supply to Australia-wide.
Based in Sydney Australia.
Design should give impressions of trust and stability.

Slogan: "your one stop technology supplier"
*two-sided name card
*logo + slogan on the back of the card

I don't have much specific requirements, leave it to designers to come up with creative & interesting masterpiece.
The logo and business card comes in first which i would like it to be completed latest by mid of March, we will require a whole redesign of our web pages, banner design, catalogue design later part.

Goodluck & thank you for your effort.

Hello designers,

Busy week, very good return rate on the number of designs and effort put into our business card design.
I thank you all for that.
We will have to extend this project for another week to two to receive more designs and more time for me to post some updates to you all.
We are getting there, i really liked some of the designs sent but just not the perfect masterpiece we are looking for.

Cheers,
Darnell Q.

Target Market(s)

Computer Retailers, Corporate, Schools, Councils.

Industry/Entity Type

Business

Requirements
Must have
• Brevon Orbital (Australia) Pty Ltd, Darnell Quist, Managing Director, Unit C, 14-18 Pellham Road, Dunmore NSW 2461, Ph +61 2 5037 1942, M +61 4 70395216, E darnell@brevonorbital.com.au, W www.brevonorbital.com.au
Nice to have
• Keep it simple & comfortable.
Target audiences are mostly >30-40 years old range.

Example of companies in the same line:-
http://www.kzp.com.au
http://www.norvix.com.au/
http://www.supplyhaventrade.com/
http://www.quenby.com.au/
http://www.bq456.com.au/
https://www.swiftgridhub.com.au/
http://carvelo.com.au/

```html
<!DOCTYPE html>
<html lang="en">
<head>
<meta charset="utf-8">
<title>Brevon Orbital – Business Card</title>
<link rel="stylesheet" href="https://fonts.googleapis.com/css2?family=Questrial&family=Mulish:wght@700&display=swap">
<style>
  :root {
    --navy: #1d3f8f;
    --red: #e6403a;
    --grey: #9b9b9b;
    --ink-soft: #8a8a8a;
    --card: #ffffff;
    --stage: #ebe9e5;
    --ray: #ececec;
  }
  * { box-sizing: border-box; margin: 0; padding: 0; }
  html, body {
    width: 1200px; height: 900px; overflow: hidden;
    background: var(--stage);
  }
  .stage {
    width: 1200px; height: 900px;
    display: flex; flex-direction: column; align-items: center; justify-content: center;
    gap: 40px;
  }
  .card {
    position: relative;
    width: 680px; height: 388px;
    background: var(--card);
    box-shadow: 0 2px 10px rgba(0,0,0,0.12);
    font-family: "Questrial", "Century Gothic", sans-serif;
    overflow: hidden;
  }

  /* Front */
  .card-front__glow {
    position: absolute; inset: 0;
    background: radial-gradient(ellipse at 50% 55%, #ffffff 0%, #f7f7f7 45%, var(--ray) 100%);
  }
  .brand {
    position: absolute; left: 0; right: 0; top: 150px;
    text-align: center;
  }
  .brand__name {
    font-family: "Questrial", "Century Gothic", sans-serif;
    font-size: 54px; color: var(--navy); letter-spacing: -0.5px; line-height: 1;
  }
  .brand__entity {
    margin-top: 8px;
    font-size: 13px; letter-spacing: 7px; color: var(--grey); text-transform: uppercase;
  }

  /* Back */
  .back-brand {
    position: absolute; right: 44px; top: 40px; text-align: right;
  }
  .back-brand .brand__name { font-size: 34px; }
  .back-brand .brand__entity { font-size: 9px; letter-spacing: 5px; margin-top: 5px; }
  .rule {
    position: absolute; height: 1px; background: var(--red);
  }
  .rule--top { left: 40px; right: 44px; top: 148px; }
  .rule--name { left: 40px; width: 330px; top: 218px; }
  .person {
    position: absolute; left: 40px; top: 166px;
  }
  .person__name {
    font-family: "Mulish", "Century Gothic", sans-serif; font-weight: 700;
    font-size: 22px; color: var(--navy); line-height: 1.1;
  }
  .person__role { font-size: 14px; color: var(--red); margin-top: 3px; }
  .address {
    position: absolute; right: 44px; top: 162px;
    text-align: right; font-size: 14px; line-height: 1.5; color: var(--ink-soft);
  }
  .contacts {
    position: absolute; left: 52px; top: 236px;
    display: grid; grid-template-columns: 40px auto; row-gap: 6px;
    font-size: 15px; line-height: 1.3;
  }
  .contacts__key { color: var(--red); }
  .contacts__value { color: var(--navy); }
</style>
</head>
<body>
<main class="stage">
  <section class="card card-front" aria-label="Business card front">
    <div class="card-front__glow" role="img" aria-label="Soft light radial background"></div>
    <div class="brand">
      <div class="brand__name">Brevon Orbital</div>
      <div class="brand__entity">Australia Pty Ltd</div>
    </div>
  </section>

  <section class="card card-back" aria-label="Business card back">
    <div class="back-brand brand">
      <div class="brand__name">Brevon Orbital</div>
      <div class="brand__entity">Australia Pty Ltd</div>
    </div>
    <div class="rule rule--top"></div>
    <div class="person">
      <div class="person__name">Darnell Quist</div>
      <div class="person__role">Managing Director</div>
    </div>
    <div class="rule rule--name"></div>
    <address class="address" style="font-style:normal">
      Unit C, 14-18<br>Pellham Road<br>Dunmore<br>NSW 2461
    </address>
    <dl class="contacts">
      <dt class="contacts__key">P</dt><dd class="contacts__value">+61 2 5037 1942</dd>
      <dt class="contacts__key">M</dt><dd class="contacts__value">+61 4 70395216</dd>
      <dt class="contacts__key">E</dt><dd class="contacts__value">darnell@brevonorbital.com.au</dd>
      <dt class="contacts__key">W</dt><dd class="contacts__value">www.brevonorbital.com.au</dd>
    </dl>
  </section>
</main>
</body>
</html>
```